Housecleaning advertisement

We are a professional residential housecleaning service, in business since 2005, providing detailed, eco-friendly housecleaning to our clients. We are looking for a design that can be used in monthly coupon books ( 4c), quarterly local magazine (biz card sized 4c) and weekly newspaper ad (biz card sized b/w). We are looking for a retro feel - think 1940s kitchens - yellow, turquoise, bright red. we want to stress that we are a local firm, not a one-size fits all franchise. We provide very personalized service (linen changes, pet-friendly, flexible scheduling, sit down with customer prior to initial cleaning and discuss their priorities so that we know what they are looking for and deliver 110% each and every clean to them - and a a very reasonable price.) Our logo is a red car with two cleaners in it. Text for the ad :
Relax and enjoy your sparkling, clean, ready-for-company home!
Test drive our detailed, eco-friendly housecleaning
four hours for $100 (new clients only)
some bulleted points
* 100% Woman-owned and staffed. We know how to clean and tidy up - and treat your home with care and respect.
* Eco-friendly products - healthier for you and your family
* Fully insured and bonded.
415.382.9156
www.tidywrenhaus.net
Target Market(s)
Professional women ages 30-65 in the New Haven County, Ct market
Industry/Entity Type
Residential
Requirements
Nice to have
- retro 1940s 1950s

```html
<!DOCTYPE html>
<html lang="en">
<head>
<meta charset="utf-8">
<title>Tidy Wren Haus Housecleaning – Ad</title>
<link href="https://fonts.googleapis.com/css2?family=Federo&family=Roboto+Condensed:wght@300;400;700&family=Oswald:wght@600;700&family=Anton&display=swap" rel="stylesheet">
<style>
  :root {
    --page: #ffffff;
    --blue-deep: #0877bd;
    --blue-mid: #1e9ddf;
    --blue-bright: #3cb4ee;
    --sky-light: #e9f6fd;
    --sky-mid: #aad9f4;
    --title-yellow: #fbf08a;
    --phone-yellow: #fdf27a;
    --burst-yellow: #fff200;
    --relax-pink: #e5007d;
    --headline-blue: #14a0e6;
    --price-red: #e3002b;
    --ink: #111111;
    --white: #ffffff;
  }
  * { margin: 0; padding: 0; box-sizing: border-box; }
  html, body { width: 1200px; height: 600px; overflow: hidden; background: var(--page); }
  .ad {
    position: absolute; left: 10px; top: 26px; width: 1163px; height: 536px;
    background: radial-gradient(ellipse at 45% 50%, var(--blue-bright) 0%, var(--blue-mid) 45%, var(--blue-deep) 100%);
    overflow: hidden;
    font-family: "Roboto Condensed", "Arial Narrow", sans-serif;
    color: var(--white);
  }
  .spotlight-ring {
    position: absolute; left: 654px; top: -10px; width: 540px; height: 540px; border-radius: 50%;
    background: rgba(255,255,255,0.12);
  }
  .spotlight {
    position: absolute; left: 672px; top: 8px; width: 504px; height: 504px; border-radius: 50%;
    background: radial-gradient(circle at 50% 40%, var(--white) 0%, var(--sky-light) 35%, var(--sky-mid) 100%);
  }
  .tagline {
    position: absolute; left: 47px; top: 29px; font-weight: 700; font-size: 19.5px; letter-spacing: 0.1px;
  }
  .brand {
    position: absolute; left: 45px; top: 68px; font-family: "Federo", serif; color: var(--title-yellow);
    line-height: 0.92;
  }
  .brand-line1 { display: block; font-size: 63px; letter-spacing: 1px; }
  .brand-line2 { display: block; font-size: 47px; letter-spacing: 0.5px; }
  .benefits {
    position: absolute; left: 47px; top: 205px; list-style: none; font-weight: 300; font-size: 25px; line-height: 28px;
  }
  .benefits li { position: relative; padding-left: 14px; margin-bottom: 10px; }
  .benefits li::before { content: "•"; position: absolute; left: 0; top: 0; }
  .divider {
    position: absolute; left: 47px; top: 411px; width: 333px; border-top: 3px dotted rgba(10,40,80,0.55);
  }
  .phone {
    position: absolute; left: 46px; top: 425px; font-weight: 700; font-size: 52px; color: var(--phone-yellow); letter-spacing: 1px;
  }
  .web {
    position: absolute; left: 47px; top: 476px; font-weight: 400; font-size: 31px;
  }
  .burst { position: absolute; left: 465px; top: 320px; width: 166px; height: 166px; }
  .burst span {
    position: absolute; inset: 0; background: var(--burst-yellow);
  }
  .burst span:nth-child(2) { transform: rotate(22.5deg); }
  .burst span:nth-child(3) { transform: rotate(45deg); }
  .burst span:nth-child(4) { transform: rotate(67.5deg); }
  .burst-text {
    position: absolute; left: 418px; top: 322px; width: 260px; text-align: center;
    transform: rotate(-12deg); color: var(--ink); font-weight: 700; font-size: 19px; line-height: 19px;
  }
  .burst-price { display: block; font-size: 42px; line-height: 36px; color: var(--price-red); }
  .burst-note { display: block; color: var(--price-red); font-size: 18px; font-style: italic; }
  .headline {
    position: absolute; left: 700px; top: 58px; width: 450px; text-align: center; line-height: 1;
  }
  .headline-relax { display: block; font-family: "Anton", "Oswald", sans-serif; color: var(--relax-pink); font-size: 96px; line-height: 92px; }
  .headline-rest { display: block; font-family: "Oswald", sans-serif; font-weight: 700; color: var(--headline-blue); font-size: 44px; line-height: 42px; text-transform: uppercase; }
  .mascot-art {
    position: absolute; left: 690px; top: 300px; width: 460px; height: 220px; border-radius: 40px;
    background: linear-gradient(180deg, #d9eef9 0%, #7fb6d8 45%, #e2423a 75%, #b62a26 100%);
    opacity: 0.9;
  }
</style>
</head>
<body>
  <main class="ad">
    <div class="spotlight-ring"></div>
    <div class="spotlight"></div>

    <p class="tagline">Test drive our detailed, eco-friendly service 4-Hour Housecleaning</p>
    <h1 class="brand"><span class="brand-line1">TIDY WREN HAUS</span><span class="brand-line2">HOUSECLEANING</span></h1>

    <ul class="benefits">
      <li>100% Woman-owned and staffed.<br>We know how to clean and tidy up -<br>and treat your home with care and respect.</li>
      <li>Eco-friendly products - healthier<br>for you and your family</li>
      <li>Fully insured and bonded.</li>
    </ul>
    <div class="divider"></div>
    <p class="phone">415.382.9156</p>
    <p class="web">www.tidywrenhaus.net</p>

    <div class="burst" aria-hidden="true"><span></span><span></span><span></span><span></span></div>
    <p class="burst-text">Test drive<br>our detailed,<br>eco-friendly<br>housecleaning<br>four hours for<span class="burst-price">$100</span><span class="burst-note">(new clients only)</span></p>

    <h2 class="headline">
      <span class="headline-relax">RELAX</span>
      <span class="headline-rest">and enjoy a<br>stress-free clean<br>and tidy home!</span>
    </h2>

    <div class="mascot-art" role="img" aria-label="Retro illustration of two cleaners riding in a red convertible loaded with mops, brooms and cleaning supplies"></div>
  </main>
</body>
</html>
```